Flyer für den Bereich Solarenergie
Zielgruppe
Guten Tag,
wir sind im Bereich Solarenergie tätig. Wir suchen nun Hallen mit großen Dächern, die wir anmieten können, um darauf Solaranlagen zu bauen. Wir machen dabei alles aus einer Hand. der Eigentümer muss nichts machen. Er bekommt sogar Geld von uns und das Dach ist sowieso meistens leer.
Aufgabenstellung
Wir möchten einen DINA4 Flyer den wir als PDF in Emails verschicken können. Farbdaten sollten Sie aus den Logodateien im Anhang entnehmen können. Richten Sie sich auch gerne an das Design des Logos und der Website. Dabei sollen kurz die wichtigsten Key Faktoren aufgelistet werden und das Unternehmen kurz dargestellt werden. Hier einmal die Texte:
Beschreibung zum Unternehmen:
Veltrano ist Experte für grüne Energietechnik mit über 20 Jahren Erfahrung. Mit über 1.000 zufriedenen Kunden im Bereich Photovoltaikanlagen können wir auf einen großen Erfahrungsschatz zurückgreifen. Wenn wir am Werk sind, wird nicht nur das Klima geschont, sondern auch Sie als Kunde profitieren. Mit uns wird nachhaltiges Handeln kinderleicht und gleichzeitig rentabel.
Erwirtschaften auch Sie mit Ihrem Dach nun bares Geld!
Ihre Vorteile:
- Umwelt schonen durch das Produzieren von grünem Strom
- Dach schützen vor Emissionen
- Dachsanierungen anstatt von Mietzahlungen möglich
- Keine Kosten, da wir alle Kosten der Anträge, der Anlage und aller Arbeiten übernehmen
- Mieteinnahmen generieren!
Einzige Voraussetzung:
Dachfläche mit mind. 1.500qm
Worauf warten Sie?
Nehmen Sie jetzt Kontakt auf für eine entsprechende Machbarkeitsprüfung. Natürlich ist auch das Kostenlos.
veltrano GmbH
Fennstraße 47b
48155 Münster
T: +49 176 528 914 03
E: info@veltrano-beispiel.de

```html
<!DOCTYPE html>
<html lang="de">
<head>
<meta charset="utf-8">
<title>Veltrano Flyer – Solarenergie</title>
<link href="https://fonts.googleapis.com/css2?family=Inter:wght@300;400;500;700;800&display=swap" rel="stylesheet">
<style>
  :root{
    --stage:#2d3140;
    --navy-deep:#15213a;
    --lime:#a6c40a;
    --lime-text:#a2c415;
    --footer:#96b006;
    --ink:#3b3b3b;
    --body:#555;
    --white:#fff;
    --soft:#f9f9f9;
  }
  *{box-sizing:border-box;margin:0;padding:0}
  html,body{width:1200px;height:1130px;overflow:hidden;background:var(--stage);font-family:"Inter",Arial,sans-serif}
  .flyer{position:absolute;left:208px;top:10px;width:784px;height:1110px;background:var(--white);overflow:hidden}

  .hero{position:absolute;left:0;top:0;width:784px;height:262px;
    background:linear-gradient(170deg,#c9a27a 0%,#4f6a8e 6%,#2d4468 35%,#1e2f4e 70%,var(--navy-deep) 100%)}
  .hero-accent{position:absolute;left:0;top:252px;width:608px;height:10px;background:var(--lime)}
  .brand{position:absolute;left:38px;top:48px;display:flex;align-items:center;color:var(--white);font-weight:700;font-size:24px;line-height:1}
  .brand-mark{width:14px;height:14px;background:var(--white);margin-right:10px}
  .hero-title{position:absolute;left:38px;top:129px;color:var(--white);font-weight:800;font-size:36px;letter-spacing:-.3px;line-height:44px}
  .hero-sub{position:absolute;left:38px;top:174px;color:var(--lime-text);font-weight:300;font-size:22px;line-height:30px}

  .photo{position:absolute;left:0;width:200px}
  .photo-roof{top:262px;height:308px;background:linear-gradient(180deg,#dfe6ee 0%,#c7d3e0 35%,#5f7bb0 60%,#2e4577 100%)}
  .photo-sunset{top:570px;height:361px;background:linear-gradient(180deg,#e9a550 0%,#b9864f 18%,#3d3c33 28%,#7c8594 45%,#3e4656 75%,#1f2430 100%)}

  .intro{position:absolute;left:200px;top:262px;width:584px;height:308px;background:var(--white);padding:50px 52px 0 37px}
  .intro-kicker{color:var(--lime-text);font-size:19px;font-weight:400}
  .intro-kicker b{font-weight:700}
  .intro-title{color:var(--ink);font-weight:700;font-size:22px;line-height:26px;margin-top:10px}
  .intro-text{color:var(--body);font-size:15px;line-height:23px;margin-top:16px}

  .benefits{position:absolute;left:200px;top:570px;width:584px;height:361px;background:var(--soft);padding:30px 40px 0 37px}
  .benefits-title{color:var(--ink);font-weight:700;font-size:22px}
  .benefit-list{list-style:none;margin-top:22px}
  .benefit{display:flex;align-items:flex-start;font-size:15px;line-height:24px;color:var(--body);margin-bottom:22px}
  .benefit svg{flex:0 0 20px;width:20px;height:20px;margin:2px 19px 0 5px}

  .cta{position:absolute;left:0;top:931px;width:784px;height:179px;background:var(--footer);color:var(--white)}
  .cta-title{position:absolute;left:38px;top:24px;font-weight:700;font-size:22px}
  .cta-rule{position:absolute;left:38px;top:63px;width:66px;height:3px;background:var(--white)}
  .cta-text{position:absolute;left:38px;top:95px;width:420px;font-size:15px;line-height:22px}
  .contact{position:absolute;left:499px;top:24px;font-size:15px;line-height:22px;font-style:normal}
  .contact-line{display:flex;align-items:center;margin-top:8px}
  .contact-line:first-of-type{margin-top:14px}
  .contact-line svg{width:16px;height:16px;margin-right:11px}
</style>
</head>
<body>
<main class="flyer">
  <header class="hero" role="img" aria-label="Foto: weitläufiges Solarfeld in der Abenddämmerung"></header>
  <div class="hero-accent"></div>
  <div class="brand"><span class="brand-mark"></span>Veltrano</div>
  <h1 class="hero-title">Ihr Experte für grüne Energietechnik</h1>
  <p class="hero-sub">Seit über 20 Jahren</p>

  <div class="photo photo-roof" role="img" aria-label="Foto: Solarmodule auf einem Hallendach mit Stadtsilhouette"></div>
  <div class="photo photo-sunset" role="img" aria-label="Foto: Hallendach mit Solarmodulen bei Sonnenuntergang"></div>

  <section class="intro">
    <p class="intro-kicker">Bereits ab <b>1500qm Dachfläche</b>!</p>
    <h2 class="intro-title">Erwirtschaften auch Sie mit Ihrem<br>Dach bares Geld!</h2>
    <p class="intro-text">Mit über 1.000 zufriedenen Kunden im Bereich Photovoltaikanlagen können wir auf einen großen Erfahrungsschatz zurückgreifen. Wenn wir am Werk sind, wird nicht nur das Klima geschont, sondern auch Sie als Kunde profitieren. Mit uns wird nachhaltiges Handeln kinderleicht und gleichzeitig rentabel.</p>
  </section>

  <section class="benefits">
    <h2 class="benefits-title">Ihre Vorteile.</h2>
    <ul class="benefit-list">
      <li class="benefit">
        <svg viewBox="0 0 20 20"><path d="M10 1 L18 4 V10 C18 15 14 18 10 19 C6 18 2 15 2 10 V4 Z" fill="#a6c40a"/><path d="M6 10 L9 13 L14 7" stroke="#fff" stroke-width="2" fill="none"/></svg>
        Dach schützen vor Emissionen</li>
      <li class="benefit">
        <svg viewBox="0 0 20 20"><circle cx="10" cy="10" r="9" fill="#a6c40a"/><text x="10" y="14" text-anchor="middle" font-size="10" font-family="Inter,Arial,sans-serif" font-weight="700" fill="#fff">€</text></svg>
        Mieteinnahmen generieren</li>
      <li class="benefit">
        <svg viewBox="0 0 20 20" fill="#a6c40a"><rect x="1" y="1" width="7" height="7" rx="1.5"/><rect x="12" y="12" width="7" height="7" rx="1.5"/><path d="M12 3 H17 V8" stroke="#a6c40a" stroke-width="2" fill="none"/><path d="M8 17 H3 V12" stroke="#a6c40a" stroke-width="2" fill="none"/></svg>
        Dachsanierungen anstatt von Mietzahlungen möglich</li>
      <li class="benefit">
        <svg viewBox="0 0 20 20"><path d="M12 1 L3 11 H9 L7 19 L17 8 H11 Z" fill="#a6c40a"/></svg>
        Umwelt schonen durch das Produzieren von grünem Strom</li>
      <li class="benefit">
        <svg viewBox="0 0 20 20"><path d="M7 1 H14 L18 5 V16 H7 Z" fill="#a6c40a" opacity=".6"/><path d="M3 4 H11 L15 8 V19 H3 Z" fill="#a6c40a"/><path d="M6 12 H12 M6 15 H12" stroke="#fff" stroke-width="1.5"/></svg>
        Keine Kosten, da wir alle Kosten der Anträge, der Anlage und aller Arbeiten übernehmen</li>
    </ul>
  </section>

  <footer class="cta">
    <h2 class="cta-title">Worauf warten Sie noch?</h2>
    <div class="cta-rule"></div>
    <p class="cta-text">Nehmen Sie jetzt Kontakt auf für eine entsprechende Machbarkeitsprüfung. Natürlich ist auch das Kostenlos.</p>
    <address class="contact">
      <div>veltrano GmbH<br>Fennstraße 47b, 48155 Münster</div>
      <div class="contact-line">
        <svg viewBox="0 0 16 16"><path d="M3 1 L6 1 L7 5 L5 6.5 C6 8.5 7.5 10 9.5 11 L11 9 L15 10 V13 C15 14 14 15 13 15 C6.5 14.5 1.5 9.5 1 3 C1 2 2 1 3 1 Z" fill="#fff"/></svg>
        +49 176 528 914 03</div>
      <div class="contact-line">
        <svg viewBox="0 0 16 16"><rect x="1" y="3" width="14" height="10" rx="1.5" fill="#fff"/><path d="M1.5 4 L8 9 L14.5 4" stroke="#96b006" stroke-width="1.4" fill="none"/></svg>
        info@veltrano-beispiel.de</div>
    </address>
  </footer>
</main>
</body>
</html>
```